Restaurant Website

I want to build a website for my restaurant. we specialise in Handmade Noodles and various stir fries. The cuisine is Asian Fusion.
Main colours of the website should be Red, White and Black.

I will have the logo attached, as well as. the menu.

The website should have 4 pages:

Main page
Menu page (menu should have photos)
Our story
Contact us

```html
<!DOCTYPE html>
<html lang="en">
<head>
<meta charset="utf-8">
<title>Red Ladle — Noodle House Delights</title>
<link href="https://fonts.googleapis.com/css2?family=Manrope:wght@400;500;600;700&display=swap" rel="stylesheet">
<style>
  :root{
    --red:#c8202f;
    --red-dark:#a9192a;
    --black:#111111;
    --ink:#2b2523;
    --text:#4a4a4a;
    --white:#ffffff;
    --footer:#0c0c0c;
    --bar:#1c1c1c;
    --muted:#8a8a8a;
  }
  *{box-sizing:border-box;margin:0;padding:0}
  html,body{width:1200px;height:3012px;overflow:hidden}
  body{font-family:"Manrope",sans-serif;color:var(--ink);background:var(--white);position:relative}
  a{color:inherit;text-decoration:none}
  .abs{position:absolute}
  .btn{position:absolute;display:flex;align-items:center;justify-content:center;background:var(--red);color:var(--white);border-radius:12px;font-size:18px;font-weight:500}
  .btn-light{background:var(--white);color:var(--black)}

  /* top bar */
  .topbar{left:0;top:0;width:1200px;height:41px;background:var(--black);color:#e6e6e6;font-size:15px}
  .topbar .phone{left:105px;top:11px}
  .topbar .promo{left:0;width:1200px;top:11px;text-align:center}
  .topbar .promo strong{text-decoration:underline;font-weight:600;color:var(--white)}
  .topbar .social{right:105px;top:11px;display:flex;gap:12px}
  .topbar .social span{width:17px;height:17px;border-radius:50%;background:#e6e6e6;display:block}

  /* header */
  .header{left:0;top:41px;width:1200px;height:119px;background:var(--white)}
  .brand{left:104px;top:20px;display:flex;align-items:center;gap:12px}
  .brand-mark{width:78px;height:78px;border-radius:50%;background:var(--ink);display:flex;align-items:center;justify-content:center;color:var(--white);font-weight:700;font-size:14px;text-align:center;line-height:1.1}
  .nav{left:212px;top:49px;display:flex;gap:30px;font-size:18px;font-weight:500;color:var(--black)}

  /* hero */
  .hero{left:0;top:160px;width:1200px;height:500px;background:linear-gradient(90deg,#dcdcdc 0%,#ececec 45%,#f2f2f2 60%,#f4f4f4 100%)}
  .hero-photo{left:620px;top:0;width:580px;height:500px;background:radial-gradient(ellipse at 60% 40%,#5c8b3b 0%,#6f9a4a 25%,#b97a45 40%,#e8e6e3 68%,#f0f0f0 100%)}
  .hero h1{left:138px;top:97px;font-size:58px;line-height:53px;font-weight:700;color:#2a211e;letter-spacing:-0.5px}
  .hero p{left:138px;top:234px;width:420px;font-size:18px;line-height:24px;color:var(--text)}

  /* section labels */
  .eyebrow{color:var(--red);font-size:17px;font-weight:600;letter-spacing:2.5px;text-transform:uppercase}

  /* menu */
  .menu-head{left:0;width:1200px;top:721px;text-align:center}
  .menu-head h2{font-size:33px;line-height:30px;font-weight:600;color:var(--black);margin-top:14px}
  .card{top:848px;width:317px}
  .card-photo{height:305px;border-radius:12px}
  .card h3{margin-top:23px;font-size:19px;font-weight:600;color:var(--black)}
  .card p{margin-top:18px;font-size:17px;line-height:24px;color:var(--text)}

  /* meal kits */
  .kits{left:104px;top:1461px;width:580px}
  .kits h2{margin-top:10px;font-size:32px;line-height:34px;font-weight:600;color:var(--black)}
  .kits p{margin-top:24px;width:565px;font-size:17px;line-height:24.2px;color:var(--text)}
  .kits-photo{left:742px;top:1459px;width:354px;height:424px;background:linear-gradient(180deg,#2f4a2c 0%,#cfc6b8 30%,#d8cfc1 60%,#5b3a22 100%)}
  .strip{left:108px;top:1883px;width:988px;height:249px;display:flex}
  .strip div{flex:1}

  /* support */
  .support-bg{left:0;top:2212px;width:1200px;height:448px;background:linear-gradient(90deg,#2a2420 0%,#1d1a18 45%,#151413 100%)}
  .support-art{left:12px;top:2290px;width:450px;height:400px;border-radius:50%;background:radial-gradient(circle at 55% 50%,#7a3b1c 0%,#b46a2e 45%,#e8b83a 70%,#f2d36a 78%,transparent 79%)}
  .support-title{left:584px;top:2336px;font-size:32px;line-height:30px;font-weight:600;color:var(--white)}
  .support-text{left:584px;top:2418px;width:420px;font-size:17px;line-height:24px;color:var(--white)}

  /* footer */
  .footer{left:0;top:2660px;width:1200px;height:303px;background:var(--footer);color:var(--white)}
  .footer-brand{left:88px;top:46px;width:151px;height:151px;border-radius:50%;background:#2f2f2f;border:3px solid #3b3b3b;display:flex;align-items:center;justify-content:center;font-weight:700;font-size:20px}
  .footer-about{left:88px;top:226px;width:260px;font-size:17px;line-height:23px}
  .fcol h4{color:var(--red);font-size:20px;font-weight:600;margin-bottom:14px}
  .fcol li{list-style:none;font-size:17px;line-height:22px;margin-bottom:15px;font-weight:500}
  .news p{width:270px;font-size:17px;line-height:22.5px;font-weight:500}
  .email{left:845px;top:167px;width:272px;height:47px;border-radius:24px;background:#1d1d1d;color:var(--muted);font-size:16px;display:flex;align-items:center;justify-content:center}
  .submit{left:845px;top:225px;width:272px;height:47px;border-radius:24px;background:var(--red);display:flex;align-items:center;justify-content:center;gap:8px;font-size:17px;font-weight:500}
  .copybar{left:0;top:2963px;width:1200px;height:49px;background:var(--bar);color:var(--muted);font-size:16px}
  .copybar .copy{left:82px;top:14px}
  .copybar .social{right:82px;top:13px;display:flex;gap:18px}
  .copybar .social span{width:20px;height:20px;border-radius:50%;border:1.5px solid var(--muted);display:block}
</style>
</head>
<body>

<div class="topbar abs">
  <div class="promo abs">Lorem ipsum dolor sit amet, consectetur &nbsp;- &nbsp;<strong>adipiscing elit.</strong></div>
  <div class="phone abs">(555) 010-2040</div>
  <div class="social abs" aria-label="Social links"><span></span><span></span><span></span><span></span></div>
</div>

<header class="header abs">
  <a class="brand abs" href="#"><span class="brand-mark">Red<br>Ladle</span></a>
  <nav class="nav abs"><a href="#">Our Menu</a><a href="#">Our Story</a><a href="#">Contact</a></nav>
  <a class="btn" href="#" style="left:947px;top:28px;width:149px;height:63px">Get Started</a>
</header>

<section class="hero abs">
  <div class="hero-photo abs" role="img" aria-label="Bowl of fresh greens with tofu and red onion"></div>
  <h1 class="abs">Noodle House<br>Delights</h1>
  <p class="abs">Lorem ipsum dolor sit amet, consectetur adipiscing elit. Tempus sit egestas a, et ante urna, in pellentesque nunc.</p>
  <a class="btn" href="#" style="left:138px;top:337px;width:149px;height:63px">Order Meal</a>
</section>

<section>
  <div class="menu-head abs">
    <div class="eyebrow">Our Menu</div>
    <h2>Noodle Creations and Stir-Fry<br>Delights Menu</h2>
  </div>
  <article class="card abs" style="left:104px">
    <div class="card-photo" role="img" aria-label="Stir-fried potatoes with peppers on a white plate" style="background:linear-gradient(135deg,#d9d9d9,#c99a4e 50%,#e8e8e8)"></div>
    <h3>Lorem ipsum dolor sit amet</h3>
    <p>Our chefs bring high standards<br>to crafting your meals.</p>
  </article>
  <article class="card abs" style="left:442px">
    <div class="card-photo" role="img" aria-label="Julienned vegetable stir-fry on a plate over wood" style="background:radial-gradient(circle,#c9452a 0%,#e9e4dc 40%,#e2ddd5 55%,#5a3522 75%)"></div>
    <h3>Lorem ipsum dolor sit amet</h3>
    <p>80% of ingredients come<br>directly from producers.</p>
  </article>
  <article class="card abs" style="left:779px">
    <div class="card-photo" role="img" aria-label="Bowls of stir-fry and fresh noodles on a red surface" style="background:linear-gradient(90deg,#4a3a30 0%,#8c8c8c 30%,#efe8d8 65%,#b9232c 100%)"></div>
    <h3>Lorem ipsum dolor sit amet</h3>
    <p>Get boxes on your schedule.<br>Skip, pause, or cancel anytime.</p>
  </article>
  <a class="btn" href="#" style="left:508px;top:1290px;width:184px;height:63px">View Full Menu</a>
</section>

<section>
  <div class="kits abs">
    <div class="eyebrow">Best Meal Kits</div>
    <h2>Lorem ipsum dolor sit amet<br>elit On The Run Meals</h2>
    <p>Lorem ipsum dolor sit amet, consectetur adipiscing elit. Sit elementum gravida malesuada facilisis suspendisse egestas mi, etiam magna. Proin tellus et amet eget. Nulla nunc lorem semper sodales hac eu diam. Eget mauris id purus consectetur donec. Tortor laoreet maecenas faucibus sed leo. Nullam hendrerit consectetur lectus amet id sed dui. Integer pellentesque quis a non consequat ut lorem nullam. Elementum risus dictum in augue sem sagittis cursus.</p>
  </div>
  <a class="btn" href="#" style="left:104px;top:1781px;width:178px;height:64px">Meal Kits</a>
  <div class="kits-photo abs" role="img" aria-label="Glass of creamy drink on a wooden table"></div>
  <div class="strip abs">
    <div role="img" aria-label="Fried rice with corn and vegetables" style="background:radial-gradient(circle,#e0a030,#c97a22 60%,#3a3a3a)"></div>
    <div role="img" aria-label="Stir-fried green beans with chili" style="background:radial-gradient(circle,#4f6b2a,#8a3a24 55%,#d8d8d8)"></div>
    <div role="img" aria-label="Steamed dumplings" style="background:radial-gradient(circle,#e0d6b8,#b9ad88 50%,#3a4a45)"></div>
    <div role="img" aria-label="Glazed chicken skewers" style="background:radial-gradient(circle,#a0401e,#7a2a16 55%,#d9d2cc)"></div>
    <div role="img" aria-label="Noodles with peppers in a bowl" style="background:radial-gradient(circle,#e8b540,#c84628 50%,#4a4a4a)"></div>
  </div>
</section>

<section>
  <div class="support-bg abs"></div>
  <div class="support-art abs" role="img" aria-label="Illustrated bowl of noodle soup with chopsticks"></div>
  <h2 class="support-title abs">Need help?<br>Contact us to get support</h2>
  <p class="support-text abs">Lorem ipsum dolor sit amet, consectetur adipiscing elit. Sit elementum gravida malesuad</p>
  <a class="btn" href="#" style="left:584px;top:2485px;width:178px;height:63px">Contact us</a>
  <a class="btn btn-light" href="#" style="left:776px;top:2485px;width:178px;height:63px">FAQs</a>
</section>

<footer class="footer abs">
  <div class="footer-brand abs">Red Ladle</div>
  <p class="footer-about abs">Lorem ipsum dolor sit amet, consectetur adipiscing elit</p>
  <div class="fcol abs" style="left:461px;top:50px">
    <h4>Our Company</h4>
    <ul><li>Our Menu</li><li>Our Story</li><li>About</li></ul>
  </div>
  <div class="fcol abs" style="left:695px;top:50px">
    <h4>About</h4>
    <ul><li>Support</li><li>Contact</li><li>Terms</li><li>Blog</li></ul>
  </div>
  <div class="fcol news abs" style="left:850px;top:50px">
    <h4>Subscribe to our Newsletter</h4>
    <p>Lorem ipsum dolor sit amet, consectetur adipiscing elit, sed do eiusmod</p>
  </div>
  <div class="email abs">Enter email address</div>
  <div class="submit abs">Submit
    <svg width="20" height="14" viewBox="0 0 20 14" fill="none" stroke="#fff" stroke-width="2" stroke-linecap="round" stroke-linejoin="round"><path d="M1 7h17M12 1l6 6-6 6"/></svg>
  </div>
</footer>

<div class="copybar abs">
  <div class="copy abs">Copyright © 2022</div>
  <div class="social abs" aria-label="Social links"><span></span><span></span><span></span><span></span></div>
</div>

</body>
</html>
```